Creative, Modern and Conversion based Web Design

Kolvex Digital has recently launched a new logo and as part of our companies rebranding, we need a new website aimed towards the UK B2B marketplace.

The website needs to deliver a modern and creative website design whilst ensuring the design is tailored towards conversion optimisation.

This site must drive point of contact either from an online form, via a direct telephone call or Skype connection.

Our sales are all offline so the website will be a simple, elegant and stunning information portal.

Kolvex Digital offers Digital Marketing services to companies throughout the UK - our target audiences are companies that turnover a minimum of 3 million pounds a year and as such we need to deliver a professional image that installs confidence in our companies abilities.

We do not like websites that are reliant upon stock photography - we are happy for stock photography to be used in a small way however the site must not look like a template filled with stock photography.

What do we do

We supply digital marketing services to those companies who demand a strong return on investment - our company prides itself on delivering successful campaigns that help establish long-term profitable relationships.

A lot of the information presented on our old site is relevant today however the design sucks. So please use the information on our current website as a foundation for your design content.

I am looking for several page designs including

"Home Page" Desktop Version
"Service Page" Desktop Version
"Blog Page" Desktop Version

"Home Page" Mobile Version
"Service Page" Mobile Version
"Blog Page" Mobile Version

In the 1st instance please only submit a single design for the "Home Page" Desktop Version - those designers that we are impressed with will be asked to complete the other designs before a winner is selected.

I like modern clean fonts - the site needs to welcome the reader and encourage them to absorb the information - not to overload and make them leave.

The site must be designed to naturally fit our companies new logo.

NO TEMPLATES

Target Market(s)

B2b - 3 million turnover and above

Industry/Entity Type

Digital Marketing

Number of Pages Required

3 page

Requirements
Must have
• Blended well with the companies logo
• We need conversion optimisation to be a huge part of the design - we considered a conversation when a potential customer reaches out to use via - web form, telephone or skype
• The current content on the old website fits today's business but the design sucks.
• www.kolvexdigital-example.com
Nice to have
• We need 3 pages (in 2 variants Desktop and Mobile)
• Home Page
• Service Page
• Blog Page
• Please only deliver the "Home Page" desktop version - if we are happy with your design we will aks for the additional pages
Should not have
• No templates and not stock photo heavy design

```html
<!DOCTYPE html>
<html lang="en">
<head>
<meta charset="utf-8">
<title>Kolvex Digital – Digital Marketing</title>
<link href="https://fonts.googleapis.com/css2?family=Lato:wght@400;700;900&family=Open+Sans:wght@400;600;700&display=swap" rel="stylesheet">
<style>
:root{
  --blue:#1a4ba6;
  --blue-dark:#0f3a8c;
  --navy:#153d8a;
  --ink:#1d1d1d;
  --text:#666;
  --grey-card:#6b6b6b;
  --light:#f3f3f3;
  --footer:#2b2b2b;
  --white:#fff;
  --faint:#ececec;
}
*{box-sizing:border-box;margin:0;padding:0}
html,body{width:1200px;height:3462px;overflow:hidden}
body{font-family:"Open Sans",Arial,sans-serif;color:var(--text);background:var(--white);position:relative}
.abs{position:absolute}
h1,h2,h3,h4{font-family:"Lato",Arial,sans-serif;color:var(--ink)}

/* Header */
.topbar{left:670px;top:0;width:530px;height:46px;background:var(--navy);color:#fff;font-size:15px;display:flex;align-items:center;gap:22px;padding-left:50px;clip-path:polygon(30px 0,100% 0,100% 100%,0 100%)}
.topbar span{display:flex;align-items:center;gap:8px}
.logo{left:99px;top:32px;width:150px}
.logo-box{border:4px solid #555;height:56px;display:flex;align-items:center;justify-content:center;font-family:"Lato",sans-serif;font-weight:900;font-size:26px;color:#555;letter-spacing:1px}
.logo-sub{font-family:"Lato",sans-serif;font-size:12px;letter-spacing:4px;color:#555;text-align:center;margin-top:5px;font-weight:700}
.nav{right:99px;top:84px;display:flex;gap:34px;font-family:"Lato",sans-serif;font-weight:700;font-size:15px;color:#333;align-items:center}

/* Hero */
.hero{left:0;top:138px;width:1200px;height:554px;background:radial-gradient(ellipse at 70% 40%,#2a62c4 0%,var(--blue) 45%,var(--blue-dark) 100%);overflow:hidden}
.hero-title{left:99px;top:178px;font-family:"Lato",sans-serif;font-size:48px;color:#fff;font-weight:400}
.hero-title b{font-weight:900}
.hero-sub{left:99px;top:250px;width:440px;color:#fff;font-size:16px;font-weight:600;line-height:30px}
.btn-outline{left:99px;top:337px;width:169px;height:46px;border:2px solid #fff;color:#fff;font-family:"Lato",sans-serif;font-weight:700;font-size:15px;display:flex;align-items:center;justify-content:center;gap:6px}
.hero-art{left:646px;top:47px;width:440px;height:450px;border-radius:30px;background:radial-gradient(circle at 50% 50%,rgba(255,200,80,.55),rgba(255,255,255,.25) 55%,rgba(255,255,255,0) 75%)}

/* Section headings */
.ghost{font-family:"Lato",sans-serif;font-weight:900;color:var(--faint);font-size:76px;white-space:nowrap;text-align:center;left:0;width:1200px;line-height:1}
.sec-title{left:0;width:1200px;text-align:center;font-size:38px;font-weight:900}
.sec-text{left:230px;width:740px;text-align:center;font-size:13.5px;line-height:28px;color:#777}

/* Service cards */
.card{top:925px;width:305px;height:257px;background:var(--grey-card);color:#fff;text-align:center;padding-top:26px}
.card.active{background:var(--blue)}
.card h3{color:#fff;font-size:22px;font-weight:900;margin:14px 0 10px}
.card p{font-size:13px;line-height:26px;padding:0 30px}
.card-corner{right:0;bottom:0;width:58px;height:58px}

/* About */
.about{left:0;top:1286px;width:1200px;height:503px;background:var(--light);overflow:hidden}
.about-art{left:69px;top:41px;width:462px;height:427px;border-radius:24px;background:linear-gradient(150deg,#dfe8f7 0%,#c9d8f2 55%,#f4e6c9 100%)}
.about-ghost{left:1090px;top:60px;writing-mode:vertical-rl;font-family:"Lato",sans-serif;font-weight:900;font-size:70px;color:#e2e2e2;line-height:1}
.about-title{left:635px;top:88px;font-size:35px;font-weight:900;line-height:46px;width:480px}
.about-text{left:635px;top:188px;width:470px;font-size:13px;line-height:25px;color:#777}
.about-text p+p{margin-top:16px}
.btn-solid{background:var(--blue);color:#fff;font-family:"Lato",sans-serif;font-weight:700;font-size:15px;display:flex;align-items:center;justify-content:center;gap:6px}

/* Process */
.step{top:1960px;width:240px;text-align:center}
.step-circle{width:120px;height:120px;border-radius:50%;border:2px solid #ddd;background:#fff;margin:0 auto;position:relative;display:flex;align-items:center;justify-content:center}
.step-num{position:absolute;left:-16px;top:40px;width:34px;height:34px;border-radius:50%;background:#6b6b6b;color:#fff;font-family:"Lato",sans-serif;font-weight:700;font-size:14px;display:flex;align-items:center;justify-content:center}
.step-num.on{background:var(--blue)}
.step h4{font-size:19px;font-weight:900;margin-top:32px;letter-spacing:.5px}
.step p{font-size:13px;line-height:27px;color:#888;margin-top:10px}

/* CTA */
.cta{left:0;top:2273px;width:1200px;height:416px;background:linear-gradient(180deg,rgba(26,75,166,.94),rgba(21,61,138,.96)),linear-gradient(120deg,#5b6d8f,#2b3b5e);overflow:hidden}
.cta-ghost{left:0;top:55px;width:1200px;text-align:center;font-family:"Lato",sans-serif;font-weight:900;font-size:72px;color:rgba(255,255,255,.12)}
.cta-title{left:0;top:70px;width:1200px;text-align:center;color:#fff;font-size:36px;font-weight:900;line-height:46px}
.cta-text{left:280px;top:182px;width:640px;text-align:center;color:#fff;font-size:13px;line-height:26px}
.btn-white{left:517px;top:293px;width:168px;height:40px;background:#fff;color:var(--blue);font-family:"Lato",sans-serif;font-weight:900;font-size:15px;display:flex;align-items:center;justify-content:center;gap:6px}

/* Clients */
.client{top:2913px;width:178px;height:87px;border:2px solid #ddd;display:flex;align-items:center;justify-content:center;gap:8px;font-family:"Lato",sans-serif;font-weight:900;font-size:24px;color:#222}
.client i{display:block;width:14px;height:14px;background:#222}
.arrow{top:2945px;font-size:26px;color:#555;font-family:"Lato",sans-serif}

/* Footer */
.footer{left:0;top:3104px;width:1200px;height:358px;background:var(--footer);color:#ddd}
.f-logo{left:99px;top:70px;width:204px}
.f-logo .logo-box{border-color:#fff;color:#fff;height:76px;font-size:34px}
.f-logo .logo-sub{color:#fff;font-size:15px;letter-spacing:6px}
.social{left:99px;top:208px;display:flex;gap:18px}
.social i{display:block;width:26px;height:26px;background:#fff;border-radius:4px}
.f-col{top:74px;font-size:14px}
.f-col h4{color:#fff;font-size:17px;font-weight:900;margin-bottom:22px}
.f-col li{list-style:none;line-height:26px}
.f-col li::before{content:"» ";color:#aaa}
.f-news{left:801px;top:74px;width:300px;font-size:14px;line-height:26px}
.f-news h4{color:#fff;font-size:17px;font-weight:900;margin-bottom:22px}
.f-input{margin-top:18px;display:flex;height:48px}
.f-input span{flex:1;background:#fff;color:#888;font-size:14px;padding-left:14px;display:flex;align-items:center}
.f-input b{width:48px;background:var(--blue);display:flex;align-items:center;justify-content:center}
.f-rule{left:99px;top:289px;width:1002px;height:1px;background:#555}
.f-copy{left:0;top:315px;width:1200px;text-align:center;font-size:14px;color:#ddd}
</style>
</head>
<body>

<!-- Header -->
<div class="abs topbar">
  <span><svg width="14" height="14" viewBox="0 0 24 24"><path fill="#fff" d="M6.6 10.8a15 15 0 006.6 6.6l2.2-2.2c.3-.3.7-.4 1-.2 1.1.4 2.3.6 3.6.6.6 0 1 .4 1 1V20c0 .6-.4 1-1 1A17 17 0 013 4c0-.6.4-1 1-1h3.5c.6 0 1 .4 1 1 0 1.3.2 2.5.6 3.6.1.3 0 .7-.2 1z"/></svg>(+1) 555 014 2290</span>
  <span>|</span>
  <span><svg width="15" height="12" viewBox="0 0 24 18"><path fill="#fff" d="M0 0h24v18H0z"/><path d="M0 0l12 9 12-9" stroke="#153d8a" stroke-width="2" fill="none"/></svg>info@kolvexdigital-example.com</span>
</div>
<div class="abs logo">
  <div class="logo-box">KOLVEX</div>
  <div class="logo-sub">DIGITAL LTD</div>
</div>
<nav class="abs nav">
  <span>HOME</span><span>ABOUT US</span><span>OUR TEAM</span><span>SERVICES</span><span>BLOG</span><span>CONTACT US</span>
  <svg width="16" height="16" viewBox="0 0 24 24"><circle cx="10" cy="10" r="7" stroke="#333" stroke-width="3" fill="none"/><path d="M15 15l7 7" stroke="#333" stroke-width="3"/></svg>
</nav>

<!-- Hero -->
<section class="abs hero">
  <h1 class="abs hero-title"><b>KOLVEX</b> DIGITAL</h1>
  <p class="abs hero-sub">We supply digital marketing services to those companies who demand a strong return on investment.</p>
  <div class="abs btn-outline">GET STARTED <span>&#10148;</span></div>
  <div class="abs hero-art" role="img" aria-label="Isometric illustration of a computer workstation with charts, documents and small figures at work"></div>
</section>

<!-- What we do -->
<div class="abs ghost" style="top:765px">WHAT WE DO</div>
<h2 class="abs sec-title" style="top:775px">WHAT WE DO BEST...</h2>
<p class="abs sec-text" style="top:831px">Lorem ipsum dolor sit amet, consectetur adipiscing elit, sed do eiusmod tempor incididunt ut labore et dolore magna aliqua. Ut enim ad minim veniam, quis nostrud exercitation ullamco laboris nisi ut aliquip ex ea commodo consequat.</p>

<div class="abs card" style="left:99px">
  <svg width="70" height="70" viewBox="0 0 70 70" fill="none" stroke="#fff" stroke-width="2.5"><circle cx="40" cy="22" r="12"/><path d="M40 16v12M36 19h8M36 25h8"/><path d="M18 40h16l6 10v12H22L16 50z"/><path d="M24 40v-8a4 4 0 018 0v8"/></svg>
  <h3>PAY PER CLICK</h3>
  <p>Lorem ipsum dolor amet consectetur adipiscing elit, sed do eiusmod tempor incidi dunt ut labore et dolore aliqua.</p>
</div>
<div class="abs card active" style="left:448px">
  <svg width="70" height="70" viewBox="0 0 70 70" fill="none" stroke="#fff" stroke-width="2.5"><rect x="6" y="10" width="52" height="34" rx="2"/><path d="M6 18h52"/><circle cx="34" cy="32" r="9"/><path d="M40 38l14 14"/><path d="M24 56h20"/></svg>
  <h3>SEO OPTIMIZATION</h3>
  <p>Lorem ipsum dolor amet consectetur adipiscing elit, sed do eiusmod tempor incidi dunt ut labore et dolore aliqua.</p>
  <svg class="abs card-corner" viewBox="0 0 58 58"><path d="M58 0v58H0z" fill="#6b6b6b"/><path d="M32 42h14M40 36l6 6-6 6" stroke="#fff" stroke-width="3" fill="none"/></svg>
</div>
<div class="abs card" style="left:796px">
  <svg width="70" height="70" viewBox="0 0 70 70" fill="none" stroke="#fff" stroke-width="2.5"><rect x="22" y="14" width="26" height="46" rx="3"/><rect x="8" y="8" width="18" height="14" rx="2"/><rect x="46" y="6" width="18" height="14" rx="2"/><path d="M30 54h10"/><circle cx="35" cy="34" r="6"/></svg>
  <h3>SOCIAL MEDIA</h3>
  <p>Lorem ipsum dolor amet consectetur adipiscing elit, sed do eiusmod tempor incidi dunt ut labore et dolore aliqua.</p>
</div>

<!-- About -->
<section class="abs about">
  <div class="abs about-art" role="img" aria-label="Illustration of a laptop with video player, megaphone and small figures promoting online content"></div>
  <div class="abs about-ghost">ABOUT US</div>
  <h2 class="abs about-title">THE DIGITAL MARKETING DIFFERENCE IN PPC</h2>
  <div class="abs about-text">
    <p>At vero eos et accusamus et iusto odio dignissimos ducimus qui blanditiis praesentium voluptatum deleniti atque corrupti.</p>
    <p>At dolores et quas molestias excepturi sint occaecati cupiditate non provident, similique sunt in culpa qui officia deserunt mollitia animi, id est laborum et dolorum fuga. Et harum quidem rerum facilis est et expedita distinctio. Nam libero tempore, cum soluta nobis est eligendi optio cumque...</p>
  </div>
  <div class="abs btn-solid" style="left:635px;top:383px;width:159px;height:40px">READ MORE <span>&#10148;</span></div>
</section>

<!-- Working process -->
<div class="abs ghost" style="top:1862px">WORKING PROCESS</div>
<h2 class="abs sec-title" style="top:1880px">OUR WORKING PROCESS</h2>

<div class="abs step" style="left:102px">
  <div class="step-circle"><span class="step-num">01</span>
    <svg width="56" height="50" viewBox="0 0 56 50" fill="none" stroke="#1a4ba6" stroke-width="2.2"><rect x="20" y="2" width="16" height="12"/><path d="M28 14v8M8 22h40M8 22v8M28 22v8M48 22v8"/><rect x="2" y="30" width="12" height="10"/><rect x="22" y="30" width="12" height="10"/><rect x="42" y="30" width="12" height="10"/></svg>
  </div>
  <h4>PLANNING</h4>
  <p>At vero et accusamus et iusto odio qui dignissimos ducimus blanditi</p>
</div>
<div class="abs step" style="left:358px">
  <div class="step-circle"><span class="step-num">02</span>
    <svg width="56" height="50" viewBox="0 0 56 50" fill="none" stroke="#1a4ba6" stroke-width="2.2"><rect x="4" y="4" width="48" height="32" rx="2"/><path d="M10 28l10-10 8 6 14-14"/><path d="M20 46h16M28 36v10"/></svg>
  </div>
  <h4>IMPLEMENTATION</h4>
  <p>At vero et accusamus et iusto odio qui dignissimos ducimus blanditi</p>
</div>
<div class="abs step" style="left:614px">
  <div class="step-circle"><span class="step-num on">03</span>
    <svg width="56" height="50" viewBox="0 0 56 50" fill="none" stroke="#1a4ba6" stroke-width="2.2"><path d="M6 44h44"/><rect x="8" y="28" width="7" height="16"/><rect x="19" y="20" width="7" height="24"/><circle cx="38" cy="20" r="10"/><path d="M45 27l8 8"/></svg>
  </div>
  <h4>ANALYSIS</h4>
  <p>At vero et accusamus et iusto odio qui dignissimos ducimus blanditi</p>
</div>
<div class="abs step" style="left:870px">
  <div class="step-circle"><span class="step-num">04</span>
    <svg width="56" height="50" viewBox="0 0 56 50" fill="none" stroke="#1a4ba6" stroke-width="2.2"><rect x="4" y="8" width="34" height="26" rx="2"/><path d="M10 26l7-7 6 5 9-9"/><circle cx="42" cy="14" r="10"/><path d="M42 8v6l4 3"/><rect x="16" y="36" width="24" height="10"/></svg>
  </div>
  <h4>FAST RESULTS</h4>
  <p>At vero et accusamus et iusto odio qui dignissimos ducimus blanditi</p>
</div>

<!-- CTA -->
<section class="abs cta">
  <div class="abs cta-ghost">WONDERING ABOUT</div>
  <h2 class="abs cta-title">STILL WONDERING ABOUT<br>WHAT WE DO?</h2>
  <p class="abs cta-text">At vero eos et accusamus et iusto odio dignissimos ducimus qui blanditiis praesentium voluptatum deleniti atque corrupti quos dolores et quas molestias excepturi sint occaecati cupiditate non provident, similique sunt in culpa qui cum soluta nobis est eligendi optio officia deserunt mollitia animi, id est laborum et dolorum fuga.</p>
  <div class="abs btn-white">GET STARTED <span>&#10148;</span></div>
</section>

<!-- Clients -->
<div class="abs ghost" style="top:2757px">OUR CLIENTS</div>
<h2 class="abs sec-title" style="top:2771px">OUR CLIENTS</h2>
<p class="abs sec-text" style="top:2829px">Lorem ipsum dolor sit amet, consectetur adipiscing elit, sed do eiusmod tempor incididunt ut labore et dolore magna aliqua. Ut enim ad minim veniam nostrud exercitation ullamco laboris nisi ut aliquip.</p>
<div class="abs arrow" style="left:58px">&#8249;</div>
<div class="abs client" style="left:99px"><i></i>MILLWORKS</div>
<div class="abs client" style="left:305px">TORVANE</div>
<div class="abs client" style="left:511px">Greyloft</div>
<div class="abs client" style="left:717px">HALVERN</div>
<div class="abs client" style="left:923px">BIG QUARRY</div>
<div class="abs arrow" style="left:1124px">&#8250;</div>

<!-- Footer -->
<footer class="abs footer">
  <div class="abs f-logo">
    <div class="logo-box">KOLVEX</div>
    <div class="logo-sub">DIGITAL LTD</div>
  </div>
  <div class="abs social"><i></i><i></i><i></i><i></i><i></i></div>
  <div class="abs f-col" style="left:395px">
    <h4>QUICK LINKS</h4>
    <ul><li>Home</li><li>About Us</li><li>Services</li><li>Working Process</li><li>Clients</li></ul>
  </div>
  <div class="abs f-col" style="left:602px">
    <h4>RESOURCES</h4>
    <ul><li>Blog</li><li>Help</li><li>FAQs</li><li>Privacy Policy</li><li>Contact Us</li></ul>
  </div>
  <div class="abs f-news">
    <h4>NEWSLETTER SIGNUP</h4>
    <p>Subscribe our newsletter &amp; get more information about our company</p>
    <div class="f-input"><span>Email Address</span><b><svg width="22" height="22" viewBox="0 0 24 24"><path d="M2 11L22 2l-6 20-4-8z" fill="none" stroke="#fff" stroke-width="2"/><path d="M12 14l10-12" stroke="#fff" stroke-width="2"/></svg></b></div>
  </div>
  <div class="abs f-rule"></div>
  <p class="abs f-copy">Copyrights © 2018 Kolvex Digital. All Rights Reserved.</p>
</footer>

</body>
</html>
```